Business Card Design

Electrical Contracting buisness
need a buisness card relating to that buisness

Reason: Just need to discuss with partner

Industry/Entity Type

Business

Contact Information for Business Card

Dale Fenwick Electrical
0431 756 918
dalefenwick7@mailnest.example
REC 58714

```html
<!DOCTYPE html>
<html lang="en">
<head>
<meta charset="utf-8">
<title>Dale Fenwick Electrical – Business Card</title>
<link href="https://fonts.googleapis.com/css2?family=Oswald:wght@400&family=Quicksand:wght@500&display=swap" rel="stylesheet">
<style>
  :root {
    --backdrop: #e4e4e2;
    --card: #0b0b0b;
    --ink: #f4f4f4;
    --art-red: #7a2417;
    --art-amber: #a8792a;
    --art-brown: #3d261c;
  }
  * { margin: 0; padding: 0; box-sizing: border-box; }
  html, body {
    width: 1200px;
    height: 873px;
    overflow: hidden;
    background: var(--backdrop);
  }
  .canvas {
    position: relative;
    width: 1200px;
    height: 873px;
  }
  .card {
    position: absolute;
    left: 75px;
    top: 136px;
    width: 1050px;
    height: 600px;
    background: var(--card);
    border-radius: 6px;
    overflow: hidden;
    color: var(--ink);
    box-shadow: 0 10px 30px rgba(0,0,0,0.18);
  }
  .card__artwork {
    position: absolute;
    left: 145px;
    top: 20px;
    width: 760px;
    height: 420px;
  }
  .card__details {
    position: absolute;
    left: 0;
    top: 0;
    width: 100%;
    height: 100%;
    display: flex;
    flex-direction: column;
    align-items: center;
    text-align: center;
    padding-top: 78px;
  }
  .card__name {
    font-family: 'Oswald', sans-serif;
    font-weight: 400;
    font-size: 66px;
    line-height: 1.1;
    letter-spacing: 1px;
    white-space: nowrap;
  }
  .card__phone {
    margin-top: 42px;
    font-family: 'Quicksand', sans-serif;
    font-weight: 500;
    font-size: 46px;
    line-height: 1.1;
    letter-spacing: 2px;
  }
  .card__email {
    margin-top: 26px;
    font-family: 'Quicksand', sans-serif;
    font-weight: 500;
    font-size: 44px;
    line-height: 1.1;
    letter-spacing: 1px;
    white-space: nowrap;
  }
  .card__licence {
    margin-top: 84px;
    font-family: 'Quicksand', sans-serif;
    font-weight: 500;
    font-size: 32px;
    line-height: 1.1;
    letter-spacing: 1px;
  }
</style>
</head>
<body>
<main class="canvas">
  <section class="card">
    <svg class="card__artwork" viewBox="0 0 760 420" role="img" aria-label="Illustration of an electrician holding lightning bolts in front of a red V emblem">
      <defs>
        <radialGradient id="artwork-tone" cx="0.5" cy="0.5" r="0.5">
          <stop offset="0" stop-color="var(--art-red)" stop-opacity="0.75"/>
          <stop offset="0.45" stop-color="var(--art-brown)" stop-opacity="0.6"/>
          <stop offset="0.75" stop-color="var(--art-amber)" stop-opacity="0.18"/>
          <stop offset="1" stop-color="var(--card)" stop-opacity="0"/>
        </radialGradient>
      </defs>
      <ellipse cx="380" cy="210" rx="380" ry="210" fill="url(#artwork-tone)"/>
    </svg>
    <div class="card__details">
      <h1 class="card__name">[ Dale Fenwick Electrical ]</h1>
      <p class="card__phone">0431 756 918</p>
      <p class="card__email">dalefenwick7@mailnest.example</p>
      <p class="card__licence">REC 58714</p>
    </div>
  </section>
</main>
</body>
</html>
```